Création d'un modèle de compte-rendus
Besoins
Cabinet de recrutement et de conseil en Ressources Humaines, nous intervenons depuis plus de 60 ans auprès d’entreprises afin de pourvoir leurs besoins en recrutement.
Nous intervenons sur tout type de postes, du cadre dirigeant à l’ouvrier, avec une majorité de postes à responsabilités.
Dans le cadre de nos recrutements, nous envoyons à l’entreprise cliente un document de synthèse des candidats intéressants que nous rencontrons. Dans ce document, nous présentons son parcours professionnel, ses informations générales (mobilité, préavis, rémunération…), ses principaux traits de personnalité, son potentiel intellectuel ainsi qu’une conclusion présentant les points forts, les axes de progrès et notre avis sur ce candidat.
Nos synthèses actuelles sont sous la forme d’un document WORD de 4 à 6 pages assez classique et nous souhaiterions avoir un document plus dynamique, tout en restant sobre. Les informations clés doivent être rapides à identifier et accessibles à l’œil facilement.
La cible :
Directeurs Généraux, Directeurs des Ressources Humaines, Responsable Recrutement
Tous secteurs d’activité
Groupes internationaux, Entreprises/Industries nationales ou locales, PME/PMI
Couleurs, favoris et autres exigences :
Cf notre logo et site internet : www.travenor-exemple.fr, tons bleus et blancs principalement
Sobriété, Simplicité
Nous sommes ouverts à toute proposition créative de votre part.

```html
<!DOCTYPE html>
<html lang="fr">
<head>
<meta charset="utf-8">
<title>Synthèse candidat – Méthode de travail et autonomie</title>
<link href="https://fonts.googleapis.com/css2?family=Mulish:wght@300;400;700&display=swap" rel="stylesheet">
<style>
  :root {
    --brand: #2f7396;
    --brand-light: #6a9cc4;
    --text: #555a5e;
    --muted: #8a8f93;
    --rule: #c9ced2;
    --icon-tint: #c9d8e1;
    --paper: #ffffff;
  }
  * { margin: 0; padding: 0; box-sizing: border-box; }
  html, body { width: 1200px; height: 849px; overflow: hidden; background: var(--paper); }
  body { font-family: "Mulish", sans-serif; color: var(--text); position: relative; }

  .brand { position: absolute; left: 34px; top: 26px; display: flex; align-items: center; gap: 10px; }
  .brand-dot { width: 14px; height: 14px; border-radius: 50%; background: var(--brand-light); }
  .brand-name { font-size: 20px; font-weight: 400; color: var(--brand-light); letter-spacing: .5px; }

  .section-tab { position: absolute; left: 0; top: 176px; width: 44px; height: 32px; background: var(--brand); }
  .section-title {
    position: absolute; left: 68px; top: 178px; width: 532px;
    font-size: 23px; font-weight: 300; letter-spacing: 1.6px; color: var(--brand);
    text-transform: uppercase; padding-bottom: 10px; border-bottom: 1px solid var(--rule);
  }

  .body-text { font-size: 13.2px; line-height: 21px; text-align: justify; font-weight: 400; }
  .body-text strong { font-weight: 700; color: #3f4448; }
  .col-left { position: absolute; left: 68px; top: 236px; width: 532px; }
  .col-right { position: absolute; left: 624px; top: 506px; width: 556px; }

  .profile-frame {
    position: absolute; left: 624px; top: 190px; width: 556px; height: 290px;
    border-left: 1px dashed var(--brand); border-bottom: 1px dashed var(--brand);
  }
  .profile-visual {
    position: absolute; left: 10px; top: 0; width: 320px; height: 270px;
    background: radial-gradient(ellipse at 50% 40%, var(--icon-tint), rgba(201,216,225,0) 70%);
  }

  .footer {
    position: absolute; left: 0; right: 0; top: 760px; height: 89px;
    border-top: 1px solid #e3e6e8; font-size: 10.5px; line-height: 15px; color: var(--muted);
  }
  .footer-block { position: absolute; top: 20px; }
  .footer-web { left: 50px; color: var(--brand); }
  .footer-address { left: 226px; }
  .footer-phone { left: 444px; }
  .footer-legal { left: 612px; }
  .footer-badge { position: absolute; left: 1004px; top: 18px; width: 56px; height: 38px; background: #2c4d6e; }
  .page-number { position: absolute; left: 1134px; top: 22px; font-size: 20px; color: var(--brand); }
</style>
</head>
<body>
  <header class="brand">
    <span class="brand-dot"></span>
    <span class="brand-name">Travenor Conseil</span>
  </header>

  <div class="section-tab"></div>
  <h1 class="section-title">Méthode de travail et autonomie</h1>

  <div class="profile-frame">
    <div class="profile-visual" role="img" aria-label="Pictogramme de profil candidat avec loupe, en bleu-gris clair"></div>
  </div>

  <div class="col-left body-text">
    <p>Cuius acerbitati uxor grave accesserat incentivum, germanitate Augusti turgida supra modum, quam Hannibaliano regi fratris filio antehac Constantinus iunxerat pater. Megaera quaedam mortalis, inflammatrix saevientis adsidua, humani <strong>cruoris avida nihil mitius quam maritus; qui paulatim eruditiores facti processu temporis ad nocendum per clandestinos versutosque rumigerulos conpertis leviter addere quaedam male suetos falsa et placentia sibi discentes, adfectati regni vel artium</strong> nefandarum calumnias insontibus adfligebant.</p>
    <p>Haec ubi latius fama vulgasset missaeque relationes adsiduae Gallum Caesarem permovissent, quoniam magister equitum longius ea tempestate distinebatur, iussus comes orientis Nebridius contractis undique militaribus copiis ad eximendam periculo civitatem amplam et oportunam studio properabat ingenti, quo cognito abscessere latrones nulla re amplius memorabili gesta, dispersique ut solent avia montium petiere celsorum.</p>
  </div>

  <div class="col-right body-text">
    <p>Cyprum itidem insulam procul a continenti discretam et portuosam inter municipia crebra urbes duae faciunt claram Salamis et Paphus, altera <strong>Iovis delubris altera Veneris templo insignis, tanta autem tamque</strong> multiplici fertilitate abundat rerum omnium eadem Cyprus ut nullius externi indigens adminiculi indigenis viribus a fundamento ipso carinae ad supremos usque carbasos aedificet onerariam navem omnibusque armamentis instructam mari committat.</p>
  </div>

  <footer class="footer">
    <div class="footer-block footer-web">www.travenor-exemple.fr<br>contact@travenor-exemple.fr</div>
    <div class="footer-block footer-address">24, rue des Tanneurs<br>57000 Metz • FRANCE</div>
    <div class="footer-block footer-phone">Tél. : +33.387.410.620<br>Fax : +33.387.410.621</div>
    <div class="footer-block footer-legal">SARL au capital de 40 000€ • 512 448 207 000 14 RCS<br>Metz • 7022Z • N° FR 31 512 448 207</div>
    <div class="footer-badge"></div>
    <div class="page-number">8</div>
  </footer>
</body>
</html>
```